Finance Broker helping people meet their personal and business goals

New business card design,
1st look at the old business card so this makes sense.
I DON'T want:
the subtext "For all your Rural and Commercial Finance".
I DON'T want the: "and Management Consultant" words
I DON'T want the old phone: 07 48213957
I DON'T want the fax number: 07 45826031
I DON'T want the email address: tallowcreek@brightlink.com.au
I DON'T want the flower
What I DO want
I DO want the mobile 0451 836 209 (in larger text)
I DO want:
My name: Dennis Harwell-Lowe
I DO want: Australian Credit Licence 529164 (Tallow Creek Pty Ltd)
I DO want: Principal Finance Broker
I DO want new email: dennis@plotnextstep.com.au
I DO want address: PO Box 928, Tully Qld 4854
I DO want the existing logo (PNS on existing card)

Target Market(s)

Business Borrowers, Home Purchasers, and People wanting to finance cars and plant and equipment

Industry/Entity Type

Financial Service

Contact Information for Business Card

See project description

Font styles to use
Serif

Colors

Designer to choose colors to be used in the design.

Requirements
Must have
• See project description
Nice to have
• Black and Yellow colours
Should not have
• See project description

```html
<!DOCTYPE html>
<html lang="en">
<head>
<meta charset="utf-8">
<title>Plot Next Step – Business Card</title>
<link href="https://fonts.googleapis.com/css2?family=Alegreya+SC:wght@400;500&family=Delius&display=swap" rel="stylesheet">
<style>
  :root {
    --backdrop: #23262b;
    --card: #121212;
    --accent: #e6ea6a;
    --ink: #f2f2f2;
    --ink-soft: #d9d9d9;
    --light-band: #ffffff;
  }
  * { box-sizing: border-box; margin: 0; padding: 0; }
  html, body { width: 1200px; height: 900px; overflow: hidden; }
  body {
    background: var(--backdrop);
    position: relative;
    font-family: "Alegreya SC", Georgia, serif;
    color: var(--ink);
  }
  .card {
    position: absolute;
    width: 560px;
    height: 320px;
    background: var(--card);
    border-radius: 4px;
    box-shadow: 0 14px 30px rgba(0,0,0,.45);
    overflow: hidden;
  }
  .card--back { left: 570px; top: 80px; }
  .card--front { left: 70px; top: 490px; }

  .brand-dot {
    display: block;
    border-radius: 50%;
    background: var(--accent);
  }

  .wordmark__name {
    font-family: "Alegreya SC", Georgia, serif;
    font-weight: 400;
    color: var(--accent);
    line-height: 1.1;
  }
  .wordmark__tagline {
    font-family: "Delius", "Comic Sans MS", cursive;
    color: var(--ink);
    line-height: 1.3;
  }

  /* back */
  .card--back .wordmark { position: absolute; left: 60px; top: 78px; }
  .card--back .wordmark__name { font-size: 38px; }
  .card--back .wordmark__tagline { font-size: 15px; margin-top: 4px; }
  .card--back .brand-dot {
    position: absolute; right: 60px; bottom: 60px;
    width: 52px; height: 52px;
  }

  /* front */
  .edge-band { position: absolute; left: 0; top: 0; width: 12px; height: 100%; }
  .edge-band__accent { height: 62%; background: var(--accent); }
  .edge-band__light { height: 38%; background: var(--light-band); }

  .front-body { position: absolute; left: 48px; top: 22px; right: 30px; }
  .front-body .brand-dot { width: 34px; height: 34px; margin-bottom: 10px; }
  .front-body .wordmark__name { font-size: 26px; }
  .front-body .wordmark__tagline { font-size: 12px; margin-top: 2px; }

  .person__name {
    font-family: "Delius", "Comic Sans MS", cursive;
    color: var(--accent);
    font-size: 28px;
    margin-top: 12px;
    line-height: 1.1;
  }
  .person__role { font-size: 14px; color: var(--ink-soft); margin-top: 2px; }
  .licence { font-size: 13px; color: var(--ink-soft); margin-top: 8px; line-height: 1.3; }

  .contact-list { list-style: none; margin-top: 10px; }
  .contact-list li {
    display: flex; align-items: center; gap: 8px;
    font-size: 13px; line-height: 1.5;
  }
  .contact-list .contact--phone { font-size: 18px; }
  .contact-list svg { width: 13px; height: 13px; flex: none; }
</style>
</head>
<body>

  <section class="card card--back" aria-label="Card back">
    <div class="wordmark">
      <div class="wordmark__name">Plot Next Step</div>
      <div class="wordmark__tagline">A Member of the Tallow Creek Group</div>
    </div>
    <span class="brand-dot" aria-hidden="true"></span>
  </section>

  <section class="card card--front" aria-label="Card front">
    <div class="edge-band">
      <div class="edge-band__accent"></div>
      <div class="edge-band__light"></div>
    </div>
    <div class="front-body">
      <span class="brand-dot" aria-hidden="true"></span>
      <div class="wordmark">
        <div class="wordmark__name">Plot Next Step</div>
        <div class="wordmark__tagline">A Member of the Tallow Creek Group</div>
      </div>
      <div class="person">
        <div class="person__name">Dennis Harwell-Lowe</div>
        <div class="person__role">Principal Finance Broker</div>
      </div>
      <div class="licence">Australian Credit Licence 529164<br>(Tallow Creek Pty Ltd)</div>
      <ul class="contact-list">
        <li class="contact--phone">
          <svg viewBox="0 0 16 16" aria-hidden="true"><circle cx="8" cy="8" r="7" fill="none" stroke="#e6ea6a" stroke-width="1.5"/><path d="M5.5 4.5l1.5 0 .6 2-1 .8a5 5 0 0 0 2.1 2.1l.8-1 2 .6v1.5c-3.5.3-6.3-2.5-6-6z" fill="#e6ea6a"/></svg>
          0451 836 209
        </li>
        <li>
          <svg viewBox="0 0 16 16" aria-hidden="true"><rect x="1.5" y="3.5" width="13" height="9" fill="none" stroke="#e6ea6a" stroke-width="1.5"/><path d="M1.5 3.5L8 9l6.5-5.5" fill="none" stroke="#e6ea6a" stroke-width="1.5"/></svg>
          dennis@plotnextstep.com.au
        </li>
        <li>
          <svg viewBox="0 0 16 16" aria-hidden="true"><path d="M8 1.5L1 8h2.2v6.5h3.6v-4h2.4v4h3.6V8H15z" fill="#e6ea6a"/></svg>
          PO Box 928, Tully Qld 4854
        </li>
      </ul>
    </div>
  </section>

</body>
</html>
```